Medical VIP club - small design

Please read the specs in a design brief attached. Also we don't have logo in a Vector format and attaching the only version we have.

Industry/Entity Type

Club

```html
<!DOCTYPE html>
<html lang="en">
<head>
<meta charset="utf-8">
<title>Medaviv – VIP Medical Club</title>
<link rel="stylesheet" href="https://fonts.googleapis.com/css2?family=Lora:ital,wght@1,700&family=Open+Sans:wght@400;600;700&display=swap">
<style>
:root{
  --stone:#b5aea7;
  --cocoa:#735a4d;
  --cocoa-deep:#8b6b5f;
  --panel:#3a2b29;
  --footer:#2e2422;
  --ink:#111;
  --cream:#f2ece6;
  --tan:#b88d72;
  --nav-top:#6a5f5b;
  --nav-bottom:#3e3431;
  --nav-active:#a39a94;
}
*{box-sizing:border-box;margin:0;padding:0}
html,body{width:1200px;height:843px;overflow:hidden}
body{position:relative;background:var(--stone);font-family:"Open Sans",Arial,sans-serif}
.brand{position:absolute;left:64px;top:40px;display:flex;align-items:center;gap:12px}
.brand-dot{width:40px;height:40px;border-radius:50%;background:var(--cocoa)}
.brand-name{font-family:"Open Sans",Arial,sans-serif;font-weight:700;font-size:50px;color:var(--cocoa);line-height:1}
.brand-tag{position:absolute;left:116px;top:98px;font-size:17px;font-weight:600;color:var(--cocoa)}
.contact-now{position:absolute;right:96px;top:46px;font-family:"Lora",Georgia,serif;font-style:italic;font-weight:700;font-size:22px;color:var(--ink)}
.call{position:absolute;right:69px;top:70px;font-family:"Lora",Georgia,serif;font-style:italic;font-weight:700;font-size:38px;color:var(--ink)}
.nav{position:absolute;left:64px;top:129px;width:1070px;height:42px;display:flex;background:linear-gradient(var(--nav-top),var(--nav-bottom));border:1px solid #cfc8c2;border-bottom:none}
.nav a{flex:1;display:flex;align-items:center;justify-content:center;font-family:"Lora",Georgia,serif;font-style:italic;font-weight:700;font-size:21px;color:#fff;text-decoration:none;border-right:1px solid #7d716c}
.nav a:last-child{border-right:none}
.nav a.active{background:linear-gradient(#bab2ac,var(--nav-active));color:#4a3f3b}
.band{position:absolute;left:0;top:171px;width:1200px;height:326px;background:var(--cocoa)}
.slide-photo{position:absolute;left:66px;top:173px;width:561px;height:324px;background:linear-gradient(120deg,#c8704a,#9a3b24 55%,#e0b58e)}
.slide-panel{position:absolute;left:627px;top:173px;width:507px;height:324px;background:var(--panel)}
.slide-title{position:absolute;left:39px;top:20px;font-family:"Lora",Georgia,serif;font-style:italic;font-weight:700;font-size:44px;color:#ddd6d2;text-shadow:2px 2px 2px #000}
.points{position:absolute;left:42px;top:88px;list-style:none}
.points li{display:flex;align-items:center;gap:12px;height:34px;font-family:"Lora",Georgia,serif;font-style:italic;font-weight:700;font-size:19px;color:#fff}
.read-more{position:absolute;left:325px;top:204px;width:104px;height:37px;border-radius:6px;background:var(--tan);color:#fff;font-size:15px;font-weight:600;display:flex;align-items:center;justify-content:center;box-shadow:0 1px 3px #000}
.dots{position:absolute;left:370px;top:284px;display:flex;gap:1px}
.dots span{width:24px;height:24px;border-radius:50%;background:#fff}
.dots span.on{background:var(--tan);border:2px solid #fff}
.card-band{position:absolute;left:66px;top:527px;width:1066px;height:181px;border-radius:14px;background:var(--cocoa-deep)}
.card{position:absolute;top:519px;width:193px;height:193px;border-radius:14px;overflow:hidden}
.card-caption{position:absolute;left:0;bottom:0;width:100%;height:46px;background:rgba(40,32,30,.72);color:#fff;font-size:17px;line-height:20px;display:flex;align-items:center;justify-content:center;text-align:center}
.divider{position:absolute;left:0;top:742px;width:1200px;border-top:2px dashed #8f8681}
.footer{position:absolute;left:0;top:745px;width:1200px;height:98px;background:var(--footer)}
.footer-nav a{position:absolute;top:27px;font-size:11px;font-weight:700;color:#d8d0cb;text-decoration:none}
.copyright{position:absolute;left:67px;top:59px;font-size:13px;color:#d8d0cb}
.find-us{position:absolute;left:461px;top:55px;font-size:17px;color:#d8d0cb}
.social{position:absolute;top:54px;width:30px;height:30px;border-radius:6px}
.footer-brand{position:absolute;left:952px;top:28px;display:flex;align-items:center;gap:8px}
.footer-brand .brand-dot{width:26px;height:26px}
.footer-brand .brand-name{font-size:34px}
</style>
</head>
<body>
<header>
  <div class="brand"><span class="brand-dot"></span><span class="brand-name">Medaviv</span></div>
  <div class="brand-tag">Medical Club</div>
  <div class="contact-now">Contact Us Now</div>
  <div class="call">Call : 555-014-200</div>
  <nav class="nav">
    <a href="#">Home</a><a href="#">VIP Club</a><a href="#" class="active">Our Services</a><a href="#">Registration</a><a href="#">Packeges</a><a href="#">Contact Us</a>
  </nav>
</header>

<section class="band"></section>
<div class="slide-photo" role="img" aria-label="Luxurious private hospital suite with bed, chandelier and sofa"></div>
<div class="slide-panel">
  <h2 class="slide-title">VIP Club</h2>
  <ul class="points">
    <li><svg width="24" height="24" viewBox="0 0 24 24"><polygon points="12,1 15,9 23,9 17,14 19,23 12,18 5,23 7,14 1,9 9,9" fill="#b5a9a2"/></svg>Lorem ipsum dolor sit amet, consetetur ....</li>
    <li><svg width="24" height="24" viewBox="0 0 24 24"><polygon points="12,1 15,9 23,9 17,14 19,23 12,18 5,23 7,14 1,9 9,9" fill="#b5a9a2"/></svg>Lorem ipsum dolor sit amet, consetetur ....</li>
    <li><svg width="24" height="24" viewBox="0 0 24 24"><polygon points="12,1 15,9 23,9 17,14 19,23 12,18 5,23 7,14 1,9 9,9" fill="#b5a9a2"/></svg>Lorem ipsum dolor sit amet, consetetur ....</li>
  </ul>
  <a class="read-more">Read More</a>
  <div class="dots"><span class="on"></span><span></span><span></span><span></span><span></span></div>
</div>

<section>
  <div class="card-band"></div>
  <div class="card" style="left:73px;background:linear-gradient(160deg,#e8ddd6,#4f8fc0)" role="img" aria-label="Team of medical staff in scrubs"><div class="card-caption">Variety Experienced<br>Doctors</div></div>
  <div class="card" style="left:289px;background:linear-gradient(160deg,#c9b59a,#5e4a3c)" role="img" aria-label="Hotel bedroom"><div class="card-caption">Hotel Services</div></div>
  <div class="card" style="left:503px;background:linear-gradient(160deg,#3b3b44,#e8e4e2 55%,#5a5a60)" role="img" aria-label="Emergency entrance sign"><div class="card-caption">Emergenct Plans</div></div>
  <div class="card" style="left:718px;background:linear-gradient(160deg,#4a4a4a,#d8d8d8 50%,#3a3a3a)" role="img" aria-label="Ambulances parked in a garage"><div class="card-caption">Transport</div></div>
  <div class="card" style="left:932px;background:linear-gradient(160deg,#eae8e6,#9c9894)" role="img" aria-label="Fountain pen on a contract"><div class="card-caption">Register Here</div></div>
</section>

<div class="divider"></div>
<footer class="footer">
  <nav class="footer-nav">
    <a href="#" style="left:64px">Home</a><a href="#" style="left:135px">VIP Club</a><a href="#" style="left:229px">Our Services</a><a href="#" style="left:343px">Registration</a><a href="#" style="left:459px">Packeges</a><a href="#" style="left:552px">Contact Us</a>
  </nav>
  <div class="copyright">Copyright © 2011 medaviv. All Right Reserve</div>
  <div class="find-us">Find Us:</div>
  <span class="social" style="left:546px;background:#5fb7e0"></span>
  <span class="social" style="left:582px;background:#3e67b0"></span>
  <span class="social" style="left:619px;background:#e8742c"></span>
  <div class="footer-brand"><span class="brand-dot"></span><span class="brand-name">Medaviv</span></div>
</footer>
</body>
</html>
```